website for shopify

build health and beauty eCommerce site...UPSCALE DESIGN PLEASE VERY FANCY. I SELL HAIR AND OTHER BEAUTY PRODUCTS. HAIR OILS, HEALTH PRODUCTS , TEA, MINERALS.AND ORGANIC MAKEUP. A SAMPLE WEB SITE. IS https://www.vandrelqostudio.com https://fomzelquar.com/

Target Market(s)

UNITED STATES

Number of Pages Required

5+ page

Font styles to use
Decorative
Script

Requirements
Must have
• ECOMMERCE SITE SHOPIFY. WILL BE MARKETED THROUGH INSTAGRAM AND FACEBOOK
• VELMORA IS NAME OF SITE IMAGE ATTACHED OF SAMPLE ART WORK. FEEL FREE TO MAKE CHANGES

```html
<!DOCTYPE html>
<html lang="en">
<head>
<meta charset="utf-8">
<title>Velmora — Shop</title>
<link href="https://fonts.googleapis.com/css2?family=Abel&family=Oswald:wght@400;500&family=Roboto:wght@400;500;700&display=swap" rel="stylesheet">
<style>
:root{
  --navy:#30334f;
  --footer:#373a58;
  --coral:#e4604e;
  --teal:#7fd0cf;
  --grey:#8a8c99;
  --light:#f4f4f6;
  --white:#ffffff;
  --muted:#9396ad;
}
*{box-sizing:border-box;margin:0;padding:0}
html,body{width:1200px;height:2209px;overflow:hidden;background:var(--white)}
body{font-family:"Roboto",Arial,sans-serif;color:var(--navy)}
.page{position:relative;width:1200px;height:2209px;overflow:hidden}
.abs{position:absolute}
a{color:inherit;text-decoration:none}

/* header */
.logo{left:69px;top:26px;font-family:"Abel",sans-serif;font-size:29px;line-height:34px;letter-spacing:4px;color:var(--navy);font-weight:400}
.nav{top:32px;font-family:"Abel",sans-serif;font-size:17px;color:#555a70}
.nav.active{color:var(--navy)}
.caret{display:inline-block;width:7px;height:7px;margin-left:5px;vertical-align:2px}
.account{left:1076px;top:8px;font-size:9px;color:#666}
.search{left:955px;top:31px;width:90px;height:24px;border:1px solid #d4d4d8;border-radius:2px;font-size:9px;color:#777;padding:6px 0 0 24px}
.search svg{position:absolute;left:8px;top:6px}

/* cart dropdown */
.cart{left:1013px;top:24px;width:159px;height:276px;background:var(--white);box-shadow:0 1px 6px rgba(0,0,0,.25)}
.cart .label{left:11px;top:10px;font-size:8px;color:#333}
.cart .label b{color:var(--coral);font-weight:400}
.cart .field{left:11px;top:25px;width:137px;height:19px;border:1px solid #ccc}
.cart-remove{width:12px;height:12px}
.cart-thumb{width:37px;height:36px}
.cart .name{font-size:8px;font-weight:700;color:#333}
.cart .qty{font-size:10px;color:#555}
.cart .total{left:10px;top:199px;font-size:8px;font-weight:700;color:#333}
.cart .sum{right:10px;top:197px;font-size:11px;color:#555}
.cart .rule{left:10px;top:191px;width:139px;height:1px;background:#e2e2e2}
.cart .checkout{left:10px;top:216px;width:137px;height:21px;background:var(--coral);border-radius:2px;color:#fff;font-size:8px;font-weight:700;text-align:center;line-height:21px}
.cart .view{left:10px;top:243px;font-size:8px;color:#555}
.cart .view span{color:var(--coral)}

/* hero */
.hero{left:0;top:87px;width:1200px;height:389px;background:linear-gradient(100deg,#e9eef3 0%,#d9c4b2 24%,#c99c80 40%,#7a5a48 52%,#d8b49c 62%,#6db8d8 72%,#e6eef2 84%,#cfe28a 100%)}
.hero-arrow{width:50px;height:47px;border:1px solid rgba(255,255,255,.55);background:rgba(255,255,255,.12)}
.shop-now{left:907px;top:415px;width:191px;height:41px;background:var(--teal);border-radius:2px;font-family:"Roboto",sans-serif;font-size:19px;color:var(--navy);text-align:center;line-height:41px;box-shadow:0 2px 0 #5fb2b1}
.badge{border-radius:50%;background:var(--teal);color:#fff;text-align:center;font-family:"Abel",sans-serif;transform:rotate(-28deg)}
.badge-hero{left:90px;top:438px;width:70px;height:70px;padding-top:11px}
.badge .big{font-size:25px;line-height:26px;font-weight:700;font-family:"Oswald",sans-serif}
.badge .small{font-size:10px;line-height:11px}

/* tabs + welcome */
.tab{top:503px;font-size:10px;font-weight:500;color:#9a9cab;letter-spacing:.3px}
.tab.current{color:var(--navy)}
.welcome-img{left:197px;top:530px;width:234px;height:156px;background:linear-gradient(160deg,#6fa7c9 0%,#aacde0 45%,#e9eef0 65%,#36536a 100%)}
.welcome-title{left:498px;top:558px;font-family:"Oswald",sans-serif;font-size:27px;line-height:36px;font-weight:500;color:var(--navy)}
.welcome-sub{left:498px;top:600px;font-size:9.5px;line-height:12px;font-weight:700;color:var(--navy)}
.welcome-text{left:498px;top:636px;width:475px;font-size:10px;line-height:12px;color:#555}

.divider{height:1px;background:var(--teal)}
.section-title{left:0;width:1200px;text-align:center;font-family:"Oswald",sans-serif;font-size:27px;line-height:36px;font-weight:500;letter-spacing:.5px;color:var(--navy)}

/* products */
.product{width:173px}
.product .photo{width:173px;height:215px}
.product .photo.framed{border:2px solid #d7d7dd}
.product .cat{position:absolute;top:232px;width:173px;text-align:center;font-size:10px;font-weight:700}
.product .price{position:absolute;top:248px;width:173px;text-align:center;font-size:14px;color:#444}
.product .price .now{color:var(--coral)}
.product .price s{color:#444}
.btn{position:absolute;top:274px;width:173px;height:23px;border-radius:2px;color:#fff;font-size:9.5px;font-weight:700;text-align:center;line-height:23px;box-shadow:0 2px 0 rgba(0,0,0,.2)}
.btn.dark{background:var(--navy)}
.btn.coral{background:var(--coral)}
.quick{position:absolute;left:47px;top:183px;width:80px;height:22px;border-radius:2px;font-size:8px;font-weight:700;text-align:center;line-height:22px}
.quick.light{background:#e6e6e8;color:#333}
.quick.dark{background:#2a2b2f;color:#fff}
.badge-sale{left:533px;top:847px;width:56px;height:56px;padding-top:11px;transform:rotate(28deg)}
.badge-sale .big{font-size:13px;line-height:15px;font-family:"Abel",sans-serif;font-weight:400}
.next{width:16px;height:17px;border:1px solid #777;border-radius:2px;background:#fff}
.next svg{display:block;margin:3px auto 0}

/* categories */
.see-all{left:889px;top:1256px;width:128px;height:24px;background:var(--coral);border-radius:2px;color:#fff;font-size:9px;font-weight:700;text-align:center;line-height:24px}
.category{width:173px}
.category .photo{width:173px;height:216px}
.category .name{position:absolute;top:228px;width:173px;text-align:center;font-size:9.5px;font-weight:700;color:#333}
.category .desc{position:absolute;top:250px;width:173px;text-align:center;font-size:10px;line-height:12px;color:#555}

/* footer */
.footer{left:0;top:1671px;width:1200px;height:538px;background:var(--footer);color:#fff}
.promo-title{font-family:"Oswald",sans-serif;font-weight:400;text-align:center;color:#fff}
.promo-img{width:246px;height:115px}
.foot-rule{height:1px;background:#4d5070}
.col-title{font-family:"Oswald",sans-serif;font-size:12px;font-weight:400;color:#fff;letter-spacing:.3px}
.foot-small{font-size:8.5px;line-height:11px;color:var(--muted)}
.foot-strong{font-size:10px;line-height:12px;font-weight:700;color:#fff}
.handle{color:var(--teal)}
.social{width:24px;height:24px;border-radius:50%}
.bottom-link{top:2156px;font-size:8px;color:#b8bacb}
.currency{left:961px;top:2150px;width:59px;height:23px;background:#2a2c44;color:#fff;font-size:8px;padding:7px 0 0 10px}
</style>
</head>
<body>
<div class="page">

  <!-- header -->
  <div class="abs logo">VELMORA</div>
  <a class="abs nav active" style="left:403px">Home</a>
  <a class="abs nav" style="left:486px">Shop<svg class="caret" viewBox="0 0 7 7"><path d="M1 2l2.5 2.5L6 2" fill="none" stroke="#555a70" stroke-width="1.2"/></svg></a>
  <a class="abs nav" style="left:574px">Sale<svg class="caret" viewBox="0 0 7 7"><path d="M1 2l2.5 2.5L6 2" fill="none" stroke="#555a70" stroke-width="1.2"/></svg></a>
  <a class="abs nav" style="left:657px">Blog</a>
  <a class="abs nav" style="left:730px">Contact Us</a>
  <div class="abs account">Login &nbsp;/&nbsp; Create an account</div>
  <div class="abs search">
    <svg width="11" height="11" viewBox="0 0 11 11"><circle cx="4.5" cy="4.5" r="3.4" fill="none" stroke="#555" stroke-width="1.3"/><path d="M7 7l3 3" stroke="#555" stroke-width="1.4"/></svg>
    Search
  </div>

  <!-- hero -->
  <div class="abs hero" role="img" aria-label="Two young women relaxing on a bed with pillows, looking at a laptop"></div>
  <div class="abs hero-arrow" style="left:26px;top:262px">
    <svg width="50" height="47" viewBox="0 0 50 47"><path d="M28 16l-7 7.5 7 7.5" fill="none" stroke="#fff" stroke-width="1.5"/></svg>
  </div>
  <div class="abs hero-arrow" style="left:1122px;top:262px">
    <svg width="50" height="47" viewBox="0 0 50 47"><path d="M22 16l7 7.5-7 7.5" fill="none" stroke="#fff" stroke-width="1.5"/></svg>
  </div>
  <a class="abs shop-now">SHOP NOW</a>
  <div class="abs badge badge-hero"><div class="big">30%</div><div class="small">discount</div></div>

  <!-- cart dropdown -->
  <div class="abs cart">
    <div class="abs label">Email Address <b>*</b></div>
    <div class="abs field"></div>
    <svg class="abs cart-remove" style="left:13px;top:51px" viewBox="0 0 12 12"><circle cx="6" cy="6" r="5.4" fill="#fff" stroke="#333"/><path d="M4 4l4 4M8 4l-4 4" stroke="#333" stroke-width="1.2"/></svg>
    <div class="abs cart-thumb" style="left:10px;top:64px;background:linear-gradient(160deg,#dfe9c9,#6f9a2c 60%,#3f5f18)" role="img" aria-label="Jar of green beauty cream"></div>
    <div class="abs name" style="left:56px;top:56px">BEAUTY CREAM</div>
    <div class="abs qty" style="left:56px;top:81px">$50.00 x 1</div>
    <svg class="abs cart-remove" style="left:13px;top:118px" viewBox="0 0 12 12"><circle cx="6" cy="6" r="5.4" fill="#fff" stroke="#333"/><path d="M4 4l4 4M8 4l-4 4" stroke="#333" stroke-width="1.2"/></svg>
    <div class="abs cart-thumb" style="left:10px;top:131px;background:linear-gradient(160deg,#f6efe6,#e2b48e 55%,#c88860)" role="img" aria-label="Massage oil bottle with towels"></div>
    <div class="abs name" style="left:56px;top:122px">MASSAGE OIL</div>
    <div class="abs qty" style="left:56px;top:148px">$50.00 x 1</div>
    <div class="abs rule"></div>
    <div class="abs total">TOTAL</div>
    <div class="abs sum">$100.00</div>
    <a class="abs checkout">CHECKOUT</a>
    <div class="abs view">or <span>View Cart</span></div>
  </div>

  <!-- tabs + welcome -->
  <div class="abs tab current" style="left:470px">WELCOME</div>
  <div class="abs tab" style="left:543px">MOST POPULAR</div>
  <div class="abs tab" style="left:645px">NEW PROMOTION</div>
  <div class="abs welcome-img" role="img" aria-label="Spa still life with lotion bottles, a pink lotus flower and a candle"></div>
  <h1 class="abs welcome-title">Welcome!</h1>
  <p class="abs welcome-sub">VELMORA IS A PLACE WHERE YOU CAN FIND ALL PRODUCTS FOR BETTER LIVING AND BETTER LOOK</p>
  <p class="abs welcome-text">lorem impusm lorem impusm lorem impusm lorem impusm lorem impusm lorem impusm lorem impusm lorem impusm lorem impusm lorem impusm lorem impusm lorem impusm lorem impusm</p>

  <div class="abs divider" style="left:166px;top:747px;width:413px"></div>
  <div class="abs divider" style="left:605px;top:747px;width:414px"></div>

  <!-- featured products -->
  <h2 class="abs section-title" style="top:793px">FEATURED PRODUCTS</h2>

  <div class="abs product" style="left:191px;top:854px">
    <div class="photo framed" role="img" aria-label="Chocolate body wrap being applied during a spa treatment" style="background:linear-gradient(150deg,#8a5a3c,#3e2418 45%,#d9ad8d 75%,#b98463)"></div>
    <div class="quick light">QUICK SHOP</div>
    <div class="cat">PRODUCTS</div>
    <div class="price">$50.00</div>
    <a class="btn dark">ADD TO CART</a>
  </div>
  <div class="abs product" style="left:408px;top:854px">
    <div class="photo" role="img" aria-label="Woman with a white face mask and cucumber slices on her eyes" style="background:linear-gradient(170deg,#c99a78,#eee8e1 40%,#8cae4c 55%,#d2a585 80%,#b88560)"></div>
    <div class="quick dark">QUICK SHOP</div>
    <div class="cat">PRODUCTS</div>
    <div class="price"><span class="now">$45.00</span> <s>$50.00</s></div>
    <a class="btn coral">ADD TO CART</a>
  </div>
  <div class="abs product" style="left:624px;top:854px">
    <div class="photo" role="img" aria-label="Hands applying pink nail polish" style="background:linear-gradient(160deg,#f4e6da,#e9c3a6 40%,#b4cfe0 70%,#e7a7b0)"></div>
    <div class="cat">PRODUCTS</div>
    <div class="price">$50.00</div>
    <a class="btn coral">ADD TO CART</a>
  </div>
  <div class="abs product" style="left:841px;top:854px">
    <div class="photo" role="img" aria-label="Relaxed woman lying on a massage table with a flower in her hair" style="background:linear-gradient(165deg,#8a5b3d,#c28a68 35%,#ecc7ad 60%,#f5ede6)"></div>
    <div class="cat">PRODUCTS</div>
    <div class="price">$50.00</div>
    <a class="btn coral">ADD TO CART</a>
  </div>
  <div class="abs badge badge-sale"><div class="big">SALE<br>OFF</div></div>
  <div class="abs next" style="left:1037px;top:953px">
    <svg width="8" height="9" viewBox="0 0 8 9"><path d="M2.5 1l3.5 3.5L2.5 8" fill="none" stroke="#333" stroke-width="1.2"/></svg>
  </div>

  <div class="abs divider" style="left:166px;top:1216px;width:413px"></div>
  <div class="abs divider" style="left:605px;top:1216px;width:414px"></div>

  <!-- featured categories -->
  <h2 class="abs section-title" style="top:1250px;width:1184px">FEATURED CATEGORIES</h2>
  <a class="abs see-all">SEE ALL CATEGORIES</a>

  <div class="abs category" style="left:181px;top:1309px">
    <div class="photo" role="img" aria-label="Pump bottle, bath salts jar and natural sponges" style="background:linear-gradient(180deg,#ffffff 0%,#f3efe6 35%,#d9b25a 75%,#c8c6bd)"></div>
    <div class="name">BEAUTY PRODUCT</div>
    <div class="desc">Sed ut perspiciatis unde omnis<br>iste natus voluptatem</div>
  </div>
  <div class="abs category" style="left:398px;top:1309px">
    <div class="photo" role="img" aria-label="Two dark shampoo and shower wash pump bottles" style="background:linear-gradient(180deg,#e6e4e2 0%,#5c5b5e 35%,#3e3d40 100%)"></div>
    <div class="name">HEALTHY PRODUCT</div>
    <div class="desc">Sed ut perspiciatis unde omnis<br>iste natus voluptatem</div>
  </div>
  <div class="abs category" style="left:614px;top:1309px">
    <div class="photo" role="img" aria-label="Open cream jar with a gold lid" style="background:linear-gradient(160deg,#ffffff 0%,#f4e3d3 45%,#d8a86c 60%,#f8f2ec)"></div>
    <div class="name">BEAUTY PRODUCT</div>
    <div class="desc">Sed ut perspiciatis unde omnis<br>iste natus voluptatem</div>
  </div>
  <div class="abs category" style="left:830px;top:1309px">
    <div class="photo" role="img" aria-label="Glass jar of green cream surrounded by leaves" style="background:linear-gradient(180deg,#ffffff 0%,#6f9a2c 40%,#c5d58a 70%,#ffffff)"></div>
    <div class="name">HEALTHY PRODUCT</div>
    <div class="desc">Sed ut perspiciatis unde omnis<br>iste natus voluptatem</div>
  </div>

  <!-- footer -->
  <footer class="abs footer"></footer>

  <div class="abs promo-title" style="left:174px;top:1745px;width:246px;font-size:19px">SPA &amp; MASSAGE</div>
  <div class="abs promo-title" style="left:450px;top:1732px;width:300px;font-size:25px">SPECIAL OFFERS</div>
  <div class="abs promo-title" style="left:780px;top:1748px;width:266px;font-size:19px">SPA &amp; MASSAGE</div>

  <div class="abs promo-img" style="left:174px;top:1789px;background:linear-gradient(160deg,#7a3f25,#e2b497 40%,#c98964 65%,#5a2a1a)" role="img" aria-label="Woman resting during a back massage"></div>
  <div class="abs promo-img" style="left:477px;top:1789px;background:linear-gradient(160deg,#f6ece3,#e9bfa0 40%,#a8c7d8 70%,#e4a0ad)" role="img" aria-label="Manicure with pink nail polish"></div>
  <div class="abs promo-img" style="left:780px;top:1789px;background:linear-gradient(160deg,#f7f1ea,#e6a43c 40%,#b9611e 60%,#f2e4dc)" role="img" aria-label="Honey dripping from a dipper beside rose petals"></div>
  <div class="abs badge" style="left:660px;top:1783px;width:70px;height:70px;padding-top:11px"><div class="big">30%</div><div class="small">discount</div></div>
  <div class="abs next" style="left:1034px;top:1838px;background:transparent;border-color:#c5c7d6">
    <svg width="8" height="9" viewBox="0 0 8 9"><path d="M2.5 1l3.5 3.5L2.5 8" fill="none" stroke="#fff" stroke-width="1.2"/></svg>
  </div>

  <div class="abs foot-rule" style="left:174px;top:1941px;width:845px"></div>

  <!-- blog -->
  <h3 class="abs col-title" style="left:174px;top:1953px">LATEST FROM BLOG</h3>
  <p class="abs foot-strong" style="left:174px;top:1987px;width:270px">Neque porro quisquam est, qui dolorem ipsum dolars vin quia dolor sit amet</p>
  <p class="abs foot-small" style="left:174px;top:2022px;width:285px">Ut enim ad minima veniam, quis nostrum exercitationem ullam corporis suscipit laboriosam, nisi ut aliquid ex ea commodi consequatur? Quis autem vel eum iure reprehenderit qui in ea voluptate.</p>
  <div class="abs foot-small" style="left:174px;top:2068px">
    <svg width="11" height="11" viewBox="0 0 11 11" style="vertical-align:-2px;margin-right:4px"><circle cx="5.5" cy="5.5" r="4.5" fill="none" stroke="#fff" stroke-width="1.3"/><path d="M5.5 3v2.7l1.8 1.2" fill="none" stroke="#fff" stroke-width="1.1"/></svg>Feb 22, 2019
  </div>
  <div class="abs foot-small" style="left:263px;top:2068px">
    <svg width="12" height="11" viewBox="0 0 12 11" style="vertical-align:-2px;margin-right:4px"><path d="M6 1C3 1 1 2.8 1 5s2 4 5 4c.6 0 1.1 0 1.6-.2L10 10l-.5-2.2C10.4 7.1 11 6.1 11 5c0-2.2-2-4-5-4z" fill="none" stroke="#fff" stroke-width="1.1"/></svg>20 comments
  </div>
  <div class="abs foot-rule" style="left:174px;top:2094px;width:245px"></div>

  <!-- tweets -->
  <div class="abs" style="left:480px;top:1954px;width:15px;height:15px;border-radius:50%;background:var(--teal)"></div>
  <h3 class="abs col-title" style="left:505px;top:1953px">LATEST TWEETS</h3>
  <p class="abs foot-small" style="left:477px;top:1988px;width:290px"><span class="handle">@Admin @User</span> Ut enim ad minima veniam, quis nostrum exercitationem suscipit laboriosam, nisi ut aliquid ex ea commodi consequatur?</p>
  <p class="abs foot-small" style="left:477px;top:2020px;opacity:.7">8 hours ago</p>
  <p class="abs foot-small" style="left:477px;top:2055px;width:290px"><span class="handle">@Admin</span> Ut enim ad minima veniam, quis nostrum exercitationem due suscipit laboriosam, nisi ut aliquid ex ea commodi consequatur.</p>
  <p class="abs foot-small" style="left:477px;top:2087px;opacity:.7">8 hours ago</p>

  <!-- contact -->
  <h3 class="abs col-title" style="left:780px;top:1953px">CONTACT US</h3>
  <p class="abs foot-small" style="left:780px;top:1988px;width:245px">Sed ut perspiciatis unde omnis iste natus error sit voluptatem accusantium doloremque laudantium, totam rem aperiam, eaque ipsa quae ab illo inventore veritatis.</p>
  <p class="abs foot-small" style="left:780px;top:2030px">Phone: 01 482 907<br>Email: <span style="color:#fff">care@lumessa.com</span></p>
  <div class="abs social" style="left:780px;top:2069px;background:#2d6fc4"></div>
  <div class="abs social" style="left:811px;top:2069px;background:#2aa6e0"></div>
  <div class="abs social" style="left:842px;top:2069px;background:#f0a01d"></div>
  <div class="abs social" style="left:873px;top:2069px;background:#a9abb5">
    <svg width="24" height="24" viewBox="0 0 24 24"><rect x="7" y="8.5" width="10" height="7" fill="#fff"/><path d="M7 8.5l5 4 5-4" fill="none" stroke="#a9abb5" stroke-width="1"/></svg>
  </div>

  <div class="abs foot-rule" style="left:174px;top:2139px;width:845px"></div>
  <div class="abs foot-small" style="left:174px;top:2156px;font-size:8px">© 2019 . All Rights Reserved</div>
  <a class="abs bottom-link" style="left:794px">Home</a>
  <a class="abs bottom-link" style="left:826px">Shop</a>
  <a class="abs bottom-link" style="left:857px">Sale</a>
  <a class="abs bottom-link" style="left:882px">Blog</a>
  <a class="abs bottom-link" style="left:907px">Contact Us</a>
  <div class="abs currency">USD
    <svg width="6" height="4" viewBox="0 0 6 4" style="position:absolute;right:9px;top:10px"><path d="M0 0h6L3 4z" fill="#fff"/></svg>
  </div>

</div>
</body>
</html>
```